Medical Device Packaging Project 2 of 5

We are a medical device startup company needing packaging for a total of 5 device brands. This is posting 2 of 5 and the device name is "Venmira"

Venmira is an intraocular lens for use in cataract surgery. The target market is Chinese ophthalmologists. The box should be sophisticated and upmarket.

The company name is Tordel Vision, I have included the logo in the uploaded files section. You should include the logo on the box.

I have uploaded a sample lens boxes from other companies that demonstrate the information needed to be contained on the box in terms of address, warnings, symbols, etc.

I have also uploaded the blank dieline of the boxes

You are welcome and encouraged to also submit to projects 1, 3, 4, and 5 as well. The same rules and expectations apply.

Industry/Entity Type

It Company

Requirements
Should not have
• Should not have any images of an eye or any bionic/futuristic feel to the design
• Note that the stavolens box is for text reference only. You may use the lens image but the futuristic/bionic look is NOT what we are going for with this brand. It should be traditional upmarket medical device artwork.

```html
<!DOCTYPE html>
<html lang="en">
<head>
<meta charset="utf-8">
<title>Venmira – Hydrophobic Intraocular Lens Packaging</title>
<link rel="stylesheet" href="https://fonts.googleapis.com/css2?family=Montserrat:wght@500;600&family=Syncopate:wght@700&display=swap">
<style>
  :root {
    --page-bg: #ececec;
    --panel-base: #fbf8f8;
    --wash-pink: #f2c9cc;
    --wash-soft: #f8e6e7;
    --brand-blue: #2a4f86;
    --brand-ring: #9cc8df;
    --product-rose: #c98c92;
    --lens-grey: #b9bcc0;
  }
  * { margin: 0; padding: 0; box-sizing: border-box; }
  html, body { width: 1200px; height: 782px; overflow: hidden; }
  body {
    background: var(--page-bg);
    display: flex;
    align-items: center;
    justify-content: center;
    font-family: "Montserrat", sans-serif;
  }
  .box-front {
    position: relative;
    width: 860px;
    height: 540px;
    background: var(--panel-base);
    overflow: hidden;
    box-shadow: 0 2px 10px rgba(0,0,0,0.08);
  }
  .watercolour-wash {
    position: absolute;
    inset: 0;
    background:
      radial-gradient(ellipse 60% 45% at 35% 78%, var(--wash-pink) 0%, rgba(242,201,204,0) 70%),
      radial-gradient(ellipse 50% 40% at 75% 70%, var(--wash-soft) 0%, rgba(248,230,231,0) 75%),
      linear-gradient(180deg, #ffffff 0%, var(--panel-base) 45%, #f6e3e4 100%);
  }
  .brand-mark {
    position: absolute;
    left: 76px;
    top: 90px;
    display: flex;
    align-items: center;
    gap: 14px;
  }
  .brand-mark .dot {
    width: 22px;
    height: 22px;
    border-radius: 50%;
    background: var(--brand-ring);
  }
  .brand-mark .name {
    font-family: "Montserrat", sans-serif;
    font-weight: 600;
    font-size: 30px;
    letter-spacing: 3px;
    color: var(--brand-blue);
  }
  .device-type {
    position: absolute;
    right: 44px;
    top: 112px;
    font-weight: 500;
    font-size: 17px;
    letter-spacing: 0.5px;
    color: var(--brand-blue);
  }
  .lens-visual {
    position: absolute;
    left: 456px;
    top: 150px;
    width: 330px;
    height: 290px;
  }
  .product-name {
    position: absolute;
    left: 76px;
    bottom: 90px;
    font-family: "Syncopate", sans-serif;
    font-weight: 700;
    font-size: 40px;
    letter-spacing: 4px;
    color: var(--product-rose);
    transform: rotate(-5deg);
    transform-origin: left bottom;
  }
  .product-spec {
    position: absolute;
    left: 78px;
    bottom: 46px;
    font-weight: 600;
    font-size: 19px;
    letter-spacing: 1px;
    color: var(--product-rose);
    transform: rotate(-5deg);
    transform-origin: left bottom;
  }
</style>
</head>
<body>
  <main class="box-front">
    <div class="watercolour-wash" role="img" aria-label="Soft pink watercolour wash background"></div>

    <div class="brand-mark">
      <span class="dot"></span>
      <span class="name">TORDEL VISION</span>
    </div>

    <p class="device-type">HYDROPHOBIC INTRAOCULAR LENS</p>

    <svg class="lens-visual" viewBox="0 0 330 290" role="img" aria-label="Illustration of an intraocular lens with two curved haptics">
      <defs>
        <radialGradient id="lensTone" cx="45%" cy="40%" r="60%">
          <stop offset="0%" stop-color="#f4f5f6"/>
          <stop offset="100%" stop-color="#9ea2a7"/>
        </radialGradient>
      </defs>
      <ellipse cx="165" cy="150" rx="95" ry="88" fill="url(#lensTone)" opacity="0.85"/>
    </svg>

    <h1 class="product-name">VENMIRA</h1>
    <p class="product-spec">ASPHERIC WITH 360° LENS</p>
  </main>
</body>
</html>
```